Structural Engineering Company needs ad for magazine

We are an engineering office for structural engineering in the entertainment industry. Our focus are concert stages, festival structures, grand stands and exhibition booths. Our customers are mainly from Europe, we realize the projects worldwide. Typical customers are designer, architects, stage builders, exhibition builder and technical service provider. We are creating structural analyses, technical consulting, technical drawings and risk assessment. We are working on mid size and major events.
Some technical notes:
- CMYK profile needed, minimum 300 dpi for raster graphic
- Our primary color is Petrol. Favourite is petrol, coral and grey (black). Please use palette shown below.
- Our font in documents is Myriad. Regular at 10 pt for text and Light at 16-24pt for titles.
- The format for the ad is 61 x 127 mm (portrait) or 185 x 46 mm (landscape). Which one is up to you.
To the content:
- For contact details we just want to provide our web address "falkowerk.de" and/or our e-mail "info@falkowerk.de"
- Attached are some Logo files and photos.
- The ad do not advertise a specific product. It is more a general advertisement for the company.
- The language for the ad should be German. Below are keywords in English and corresponding German translation. You do not need to place all Keywords, it is just a brainstorming list to help you. You are also welcome to use other text. We will help with translation, if necessary.
- we like discussing ideas to get better results, so also if you have questions, please ask.
- If you need information that we haven't thought of yet, please ask.
Our slogan (also in Germany): event meets engineering
Service Keywords EN / DE
- Structural Analysis / Statische Berechnungen
- Risk Assessment / Risikobewertungen
- Consulting & Design / Beratung & Konstruktion
Technical Keywords EN / DE
- Stage machinery / Bühnentechnik
- Scaffolding / Gerüstbau
- Exhibition Booths / Messebauten
- Tents / Zelte
- Temporary Structures / Fliegende Bauten
- Truss / Traversen
- Stages / Bühnen
- Grand Stands / Tribünen
- Leightweight Construction / Leichtbau
- Steel Construction / Stahlbau
- Amusement Rides / Fahrgeschäfte
Look and feel

```html
<!DOCTYPE html>
<html lang="de">
<head>
<meta charset="utf-8">
<title>Falkowerk Engineering – Anzeige</title>
<link href="https://fonts.googleapis.com/css2?family=Source+Sans+3:wght@300;400;700;800&display=swap" rel="stylesheet">
<style>
  :root {
    --sky-top: #3d6fc6;
    --sky-bottom: #9db6dc;
    --stage-grey: #7d8794;
    --violet-deep: #4a3f9e;
    --violet-mid: #7a62c4;
    --magenta-soft: #b46fc4;
    --edge-lavender: #c8cdf2;
    --band: rgba(48, 48, 58, 0.62);
    --white: #ffffff;
  }
  * { margin: 0; padding: 0; box-sizing: border-box; }
  html, body { width: 1200px; height: 298px; overflow: hidden; background: var(--sky-top); }
  body { font-family: "Source Sans 3", "Myriad Pro", sans-serif; color: var(--white); }

  .ad { position: relative; width: 1200px; height: 298px; overflow: hidden; }

  .stage-photo {
    position: absolute; inset: 0;
    background: linear-gradient(180deg, var(--sky-top) 0%, #5d8bd2 40%, var(--sky-bottom) 62%, var(--stage-grey) 100%);
  }

  .keyword-band {
    position: absolute; left: 500px; top: 192px; width: 700px; height: 76px;
    background: var(--band);
  }

  .truss-photo { position: absolute; left: 0; top: 0; width: 540px; height: 298px; }

  .services { position: absolute; left: 0; top: 0; }
  .service {
    position: absolute; white-space: nowrap;
    font-size: 28.5px; font-weight: 400; line-height: 1;
  }
  .service strong { font-weight: 800; }
  .service--statik { left: 538px; top: 17px; }
  .service--risk { left: 558px; top: 58px; }
  .service--design { left: 578px; top: 100px; }

  .contact {
    position: absolute; left: 971px; top: 24px; height: 64px;
    border-left: 2px solid var(--white); padding-left: 12px;
  }
  .contact__title { font-size: 18px; font-weight: 800; line-height: 1; letter-spacing: 0.01em; margin-top: -1px; }
  .contact__row { display: flex; align-items: center; gap: 10px; margin-top: 6px; font-size: 18.5px; line-height: 1; }
  .contact__row--web { font-weight: 800; }
  .contact__row--mail { font-weight: 400; margin-top: 7px; }
  .contact__icon { width: 18px; height: 18px; flex: none; }

  .brand-name {
    position: absolute; left: 59px; top: 124px; width: 200px;
    font-size: 20px; font-weight: 400; letter-spacing: 0.2em; line-height: 1.25;
    text-transform: uppercase;
  }

  .claim {
    position: absolute; left: 59px; top: 186px;
    font-size: 33px; font-weight: 400; line-height: 38px; white-space: nowrap;
  }
  .claim strong { font-weight: 800; }

  .keywords {
    position: absolute; left: 520px; top: 205px; width: 680px;
    text-align: center; font-size: 18.7px; font-weight: 400; line-height: 22px; white-space: nowrap;
  }
</style>
</head>
<body>
<main class="ad">
  <div class="stage-photo" role="img" aria-label="Foto einer Open-Air-Festivalbühne mit Gerüsttürmen und LED-Wänden vor blauem Himmel"></div>

  <div class="keyword-band"></div>

  <svg class="truss-photo" viewBox="0 0 540 298" role="img" aria-label="Foto einer Aluminium-Traverse mit Scheinwerfer in violettem Bühnenlicht">
    <defs>
      <linearGradient id="truss-light" x1="0" y1="0" x2="1" y2="1">
        <stop offset="0" stop-color="#6a74b8"/>
        <stop offset="0.45" stop-color="var(--violet-mid)"/>
        <stop offset="0.75" stop-color="var(--violet-deep)"/>
        <stop offset="1" stop-color="var(--magenta-soft)"/>
      </linearGradient>
    </defs>
    <path d="M0 0 H428 C450 25 470 60 495 110 C515 150 524 200 516 245 C512 270 508 285 506 298 H0 Z" fill="url(#truss-light)"/>
    <path d="M428 0 C450 25 470 60 495 110 C515 150 524 200 516 245 C512 270 508 285 506 298" fill="none" stroke="var(--edge-lavender)" stroke-width="6"/>
  </svg>

  <div class="brand-name">Falkowerk Engineering</div>

  <p class="claim"><strong>Strukturanalysen</strong> für<br>die Unterhaltungstechnik</p>

  <div class="services">
    <p class="service service--statik"><strong>Statische</strong> Berechnungen</p>
    <p class="service service--risk"><strong>Risikobewertungen</strong></p>
    <p class="service service--design"><strong>Beratung</strong> &amp; Konstruktion</p>
  </div>

  <aside class="contact">
    <p class="contact__title">KONTAKTIERE UNS</p>
    <p class="contact__row contact__row--web">
      <svg class="contact__icon" viewBox="0 0 20 20" fill="none" stroke="#fff" stroke-width="1.6">
        <circle cx="10" cy="10" r="8.2"/><ellipse cx="10" cy="10" rx="3.6" ry="8.2"/>
        <line x1="1.8" y1="10" x2="18.2" y2="10"/><path d="M3.2 5.6 H16.8 M3.2 14.4 H16.8"/>
      </svg>
      falkowerk.de
    </p>
    <p class="contact__row contact__row--mail">
      <svg class="contact__icon" viewBox="0 0 20 20" fill="none" stroke="#fff" stroke-width="1.5">
        <rect x="1.5" y="4" width="17" height="12"/><path d="M1.5 4 L10 11 L18.5 4 M1.5 16 L7.5 9.5 M18.5 16 L12.5 9.5"/>
      </svg>
      info@falkowerk.de
    </p>
  </aside>

  <p class="keywords">
    Bühnentechnik · Gerüstbau · Messebauten · Zelte · Fliegende Bauten<br>
    Traversen · Bühnen · Tribünen · Leichtbau · Stahlbau · Fahrgeschäfte
  </p>
</main>
</body>
</html>
```